I need a business card for my original fine art pieces

I would like a business card design including a logo design for a new business in the art world. I am based in the Hunter Valley NSW Australia. I am a contemporary figurative, encaustic and wildlife artist. I would like to be able to upload my email and mobile number to this as well. This design should be one that I can incorporate into banners and flyers etc. Id like to incorporate one of my own images or partial image into the background or somewhere below. My initials are KD and I would like these used as a logo type. I would like the use of some colour and it to be bright and catchy. The final design should communicate artwork custom made and commissions available.

Overview: Original Fine Artworks for sale, online, art galleries etc, Custom made to order and by commission.

Target market is world wide audience and corporate world

My figurative work is painted using acrylics in a lot of natural ochre colours that reflect the Australian Outback, on canvas, linen, paper or board: My encaustic work is created in a contemporary abstract style using a blow torch and a made with a medium of 100% pure bees wax, Damar resin, mixed media and coloured pigments, applied to Birch board. My wildlife are created using coloured pencil and mixed media on a variety of paper types or board.

```html
<!DOCTYPE html>
<html lang="en">
<head>
<meta charset="utf-8">
<title>Kara Dalton — Business Card</title>
<link rel="stylesheet" href="https://fonts.googleapis.com/css2?family=Rubik+Distressed&family=Cinzel:wght@400&family=Crimson+Text:wght@400&display=swap">
<style>
  :root {
    --backdrop: #2b2b2d;
    --card-black: #0d0e10;
    --card-steel: #1c1f24;
    --ink-ice: #e4f0fb;
    --ink-soft: #d9dde2;
    --swirl-pink: #e0308f;
    --swirl-violet: #7a3fc4;
    --swirl-blue: #2a7fd8;
    --swirl-teal: #2cc3b0;
    --swirl-green: #5fce4f;
    --swirl-yellow: #f2d23c;
    --swirl-orange: #f0702a;
  }
  html, body {
    margin: 0;
    width: 1200px;
    height: 798px;
    overflow: hidden;
    background: var(--backdrop);
  }
  .canvas {
    position: relative;
    width: 1200px;
    height: 798px;
    display: flex;
    align-items: center;
    justify-content: center;
  }
  .card {
    position: relative;
    width: 900px;
    height: 514px;
    overflow: hidden;
    background:
      repeating-linear-gradient(90deg, rgba(255,255,255,0.025) 0 1px, transparent 1px 3px),
      linear-gradient(110deg, var(--card-black) 0%, var(--card-steel) 45%, var(--card-black) 75%);
    box-shadow: 0 10px 30px rgba(0,0,0,0.45);
  }
  .card__artwork {
    position: absolute;
    top: 0;
    right: 0;
    width: 430px;
    height: 100%;
    background:
      radial-gradient(ellipse 60% 30% at 70% 20%, var(--swirl-pink), transparent 70%),
      radial-gradient(ellipse 50% 25% at 40% 45%, var(--swirl-green), transparent 70%),
      radial-gradient(ellipse 55% 30% at 80% 60%, var(--swirl-blue), transparent 70%),
      radial-gradient(ellipse 45% 25% at 55% 80%, var(--swirl-yellow), transparent 70%),
      radial-gradient(ellipse 40% 20% at 30% 92%, var(--swirl-orange), transparent 70%),
      linear-gradient(160deg, var(--swirl-violet), var(--swirl-pink) 40%, var(--swirl-teal) 70%, var(--swirl-violet));
    -webkit-mask-image: linear-gradient(90deg, transparent 0%, rgba(0,0,0,0.6) 25%, #000 45%);
    mask-image: linear-gradient(90deg, transparent 0%, rgba(0,0,0,0.6) 25%, #000 45%);
  }
  .card__identity {
    position: absolute;
    left: 90px;
    top: 62px;
    width: 420px;
    text-align: center;
  }
  .card__monogram {
    font-family: "Cinzel", Georgia, serif;
    font-weight: 400;
    font-size: 72px;
    line-height: 1;
    letter-spacing: 4px;
    color: var(--ink-ice);
    margin: 0 0 30px;
  }
  .card__name {
    font-family: "Rubik Distressed", system-ui, sans-serif;
    font-weight: 400;
    font-size: 54px;
    line-height: 1;
    color: var(--ink-ice);
    margin: 0;
    letter-spacing: 1px;
  }
  .card__tagline {
    font-family: "Cinzel", Georgia, serif;
    font-size: 22px;
    color: var(--ink-soft);
    margin: 14px 0 0;
    letter-spacing: 1px;
  }
  .card__contact {
    font-family: "Crimson Text", Georgia, serif;
    font-size: 21px;
    line-height: 1.15;
    color: var(--ink-soft);
    margin: 40px 0 0;
  }
  .card__contact span { display: block; }
</style>
</head>
<body>
<main class="canvas">
  <section class="card">
    <div class="card__artwork" role="img" aria-label="Colourful swirling abstract encaustic artwork in pink, blue, green and yellow"></div>
    <div class="card__identity">
      <div class="card__monogram">KD</div>
      <h1 class="card__name">Kara Dalton</h1>
      <p class="card__tagline">Original Fine Artworks</p>
      <p class="card__contact">
        <span>000 000 0000</span>
        <span>info@webaddress.com</span>
      </p>
    </div>
  </section>
</main>
</body>
</html>
```